Fennel's Cafe Television Menu Boards

Need a menu board to display on 2 television screens (50") in quick serve restaurant. Page one of word document is one screen and page two is the other. Please add logo where able. Would like black background for menu boards with white, green and/or red lettering where it fits. (Picture of concept is attached so you can see the restaurant space). Pictures, backgrounds and other are welcome as we look at first few designs.

Target Market(s)

Location is inside of a Dunwick Hotel and attached to a hospital. Target is hotel guests and local hospital employees.

Industry/Entity Type

Italian Café

Colors

Designer to choose colors to be used in the design.

Requirements
Must have
• Easy to read and understand
• creative design, not just a list of items
Nice to have
• black or dark background, some sort of watermark or design throughout

```html
<!DOCTYPE html>
<html lang="en">
<head>
<meta charset="UTF-8">
<title>Fennel's Cafe Menu Board</title>
<link href="https://fonts.googleapis.com/css2?family=Bebas+Neue&family=Oswald:wght@300;400&display=swap" rel="stylesheet">
<style>
  :root {
    --board: #2a2c2d;
    --board-light: #3a3d3e;
    --chalk: #f2f2ee;
    --chalk-soft: rgba(242, 242, 238, 0.75);
    --accent: #e6e02a;
    --art: #4a4d4e;
    --watermark: rgba(255, 255, 255, 0.05);
  }
  * { margin: 0; padding: 0; box-sizing: border-box; }
  html, body { width: 1200px; height: 800px; overflow: hidden; }
  body {
    background: radial-gradient(ellipse at 55% 40%, var(--board-light), var(--board) 75%);
    color: var(--chalk);
    font-family: "Oswald", sans-serif;
    font-weight: 300;
    position: relative;
  }
  .watermark {
    position: absolute; left: 330px; top: 90px; width: 400px; height: 640px;
    border-radius: 50% 50% 50% 50% / 60% 60% 40% 40%;
    background: radial-gradient(ellipse, var(--watermark), transparent 70%);
  }
  .rule { position: absolute; background: var(--chalk-soft); }
  .rule--v1 { left: 470px; top: 40px; width: 1px; height: 320px; }
  .rule--v2 { left: 770px; top: 50px; width: 1px; height: 710px; }
  .rule--h1 { left: 30px; top: 380px; width: 420px; height: 1px; }
  .rule--h2 { left: 490px; top: 385px; width: 265px; height: 1px; }
  .rule--h3 { left: 790px; top: 600px; width: 385px; height: 1px; }

  .art { position: absolute; background: var(--art); border-radius: 14px; opacity: 0.8; }

  .feature { position: absolute; text-align: center; }
  .feature__title {
    font-family: "Bebas Neue", sans-serif; font-size: 48px; line-height: 1;
    display: inline-block; padding-bottom: 6px;
    border-bottom: 2px dotted var(--accent);
  }
  .feature__price { font-size: 30px; margin: 10px 0 12px; }
  .feature__items { font-size: 17px; line-height: 1.4; text-transform: uppercase; }

  .sides { left: 90px; top: 190px; width: 290px; }
  .soup { left: 480px; top: 215px; width: 280px; }

  .section-title { position: absolute; font-family: "Bebas Neue", sans-serif; line-height: 1; white-space: nowrap; }
  .desserts-title { left: 40px; top: 430px; font-size: 86px; }
  .salads-title { left: 790px; top: 60px; font-size: 86px; }

  .price-list { position: absolute; list-style: none; text-transform: uppercase; }
  .price-row { display: flex; align-items: baseline; gap: 10px; white-space: nowrap; }
  .price-row__leader { flex: 1; border-bottom: 2px dotted var(--accent); transform: translateY(-6px); }
  .dessert-list { left: 40px; top: 540px; width: 560px; font-size: 23px; }
  .dessert-list .price-row { margin-bottom: 22px; }
  .size-list { left: 790px; top: 250px; width: 385px; font-size: 20px; }
  .size-list .price-row { margin-bottom: 4px; }

  .salad-menu { position: absolute; left: 790px; top: 340px; width: 385px; text-align: center; text-transform: uppercase; }
  .salad-menu__name { font-size: 23px; line-height: 1.3; }
  .salad-menu__name em { font-style: normal; color: var(--accent); }
  .salad-menu__desc { font-size: 9px; letter-spacing: -0.2px; white-space: nowrap; margin: 18px 0 8px; }
  .salad-menu__caprese { font-size: 16px; white-space: nowrap; }
  .salad-menu__extras { font-size: 14px; color: var(--accent); margin-top: 34px; line-height: 1.4; }

  .brand { position: absolute; left: 790px; top: 640px; width: 385px; text-align: center; font-family: "Oswald", sans-serif; font-weight: 400; font-size: 46px; color: var(--chalk); }
</style>
</head>
<body>
  <div class="watermark" role="img" aria-label="Faint large leaf watermark"></div>

  <div class="rule rule--v1"></div>
  <div class="rule rule--v2"></div>
  <div class="rule rule--h1"></div>
  <div class="rule rule--h2"></div>
  <div class="rule rule--h3"></div>

  <div class="art" style="left:170px;top:70px;width:150px;height:90px" role="img" aria-label="Chalk drawing of a baguette loaf"></div>
  <section class="feature sides">
    <h2 class="feature__title">Sides</h2>
    <p class="feature__price">0.95</p>
    <p class="feature__items">Homemade garlic bread<br>Smoked gouda garlic bread</p>
  </section>

  <div class="art" style="left:565px;top:70px;width:110px;height:120px" role="img" aria-label="Chalk drawing of a steaming cup of soup on a saucer"></div>
  <section class="feature soup">
    <h2 class="feature__title">Cup of Soup</h2>
    <p class="feature__price">$4.50</p>
    <p class="feature__items" style="font-size:15px">Cream of tomato basil</p>
  </section>

  <h2 class="section-title desserts-title">Desserts</h2>
  <ul class="price-list dessert-list">
    <li class="price-row"><span>Lemon cream cake</span><span class="price-row__leader"></span><span>$9.99</span></li>
    <li class="price-row"><span>Strawberry cheese cake</span><span class="price-row__leader"></span><span>$9.99</span></li>
    <li class="price-row"><span>Noccella chocolate nut cake</span><span class="price-row__leader"></span><span>$9.99</span></li>
  </ul>
  <div class="art" style="left:615px;top:480px;width:140px;height:210px" role="img" aria-label="Chalk drawing of a cupcake topped with a cherry"></div>

  <h2 class="section-title salads-title">Salads</h2>
  <div class="art" style="left:1010px;top:60px;width:165px;height:110px" role="img" aria-label="Chalk drawing of a salad plate with fork and knife"></div>
  <ul class="price-list size-list">
    <li class="price-row"><span>Large</span><span class="price-row__leader"></span><span>$6.95</span></li>
    <li class="price-row"><span>Small</span><span class="price-row__leader"></span><span>$4.00</span></li>
  </ul>
  <section class="salad-menu">
    <p class="salad-menu__name">Caesar <em>Salad</em></p>
    <p class="salad-menu__name">Mixed Garden <em>Salad</em></p>
    <p class="salad-menu__desc">Mixed greens, cherry tomatoes, cucumbers, carrots, parmesan cheese, Italian dressing</p>
    <p class="salad-menu__caprese">Caprese with tomatoes, mozzarella, basil olive oil</p>
    <p class="salad-menu__extras">Add chicken +$2<br>Add shrimp +$3</p>
  </section>

  <p class="brand">Fennel's</p>
</body>
</html>
```